Professional BIO Template with photo and logo

Hello,
I need a professional Bio template developed via Microsoft WORD ASAP!!!!! I would like to just be able to add the text I need to add. So resize-able text boxes. Potentially able to adjust the font. These are the things I need added it to include.
Head shot (attached)
Text Box for Name
Text Box for phone number
Text box for email
KTW Logo (attached)
Maybe a blue banner at the top or some background boxes that are blue or grey. Here are the pantone colors that our company uses.

CORE COLOR
100c 91m 17y 6k 38r 58g 128b Hex #263A80 Pantone 7687 C

CORE CONTRAST COLOR
36c 29m 28y 0k 168r 168g 170b Hex #669999 Pantone Cool Gray 6C

I also attached some examples of what we have been looking at. Instead of green add the blue...instead of black maybe just be white.

Thank you

```html
<!DOCTYPE html>
<html lang="en">
<head>
<meta charset="utf-8">
<title>Professional Bio – Daniel Mercer</title>
<link rel="stylesheet" href="https://fonts.googleapis.com/css2?family=Arimo:wght@400;700&family=Tinos:ital@1&family=Roboto+Condensed:wght@400&display=swap">
<style>
  :root {
    --core-blue: #2e3a80;
    --banner-blue: #303d82;
    --bright-blue: #1b86d6;
    --text-blue: #2d3b86;
    --body-text: #2f2f2f;
    --cool-gray: #bdbdbd;
    --frame-gray: #9a9a9a;
    --pale-blue: #cfe3f6;
    --backdrop: #e9e9ea;
    --white: #ffffff;
  }
  * { box-sizing: border-box; margin: 0; padding: 0; }
  html, body { width: 1200px; height: 1113px; overflow: hidden; background: var(--backdrop); }
  .sheet {
    position: absolute; left: 185px; top: 20px;
    width: 1127px; height: 1458px;
    transform: scale(0.7363); transform-origin: top left;
    background: var(--white);
    font-family: "Arimo", Arial, sans-serif;
    overflow: hidden;
    box-shadow: 0 6px 24px rgba(0,0,0,0.18);
  }
  .wash {
    position: absolute; left: 306px; top: 1040px; width: 821px; height: 418px;
    background: radial-gradient(ellipse at 0% 100%, var(--pale-blue) 0%, rgba(207,227,246,0.5) 35%, rgba(255,255,255,0) 75%);
  }
  .banner {
    position: absolute; left: 0; top: 177px; width: 100%; height: 146px;
    background: var(--banner-blue);
  }
  .banner-art {
    position: absolute; left: 0; top: 0; width: 580px; height: 146px;
    background: linear-gradient(100deg, #1560ad 0%, var(--bright-blue) 30%, #1f5aa8 60%, var(--banner-blue) 100%);
  }
  .headshot {
    position: absolute; left: 34px; top: 33px; width: 278px; height: 278px; border-radius: 50%;
    background: radial-gradient(circle at 50% 40%, #b98a6c 0%, #7a5a48 30%, #3d3d40 65%, #2a2a2c 100%);
  }
  .name {
    position: absolute; left: 375px; top: 120px;
    font-weight: 700; font-size: 48px; color: var(--core-blue); white-space: nowrap;
  }
  .role {
    position: absolute; left: 379px; top: 195px;
    font-family: "Tinos", "Times New Roman", serif; font-style: italic;
    font-size: 37px; color: var(--white);
  }
  .summary {
    position: absolute; left: 40px; top: 387px; width: 275px;
    font-family: "Tinos", "Times New Roman", serif; font-style: italic;
    font-size: 22.5px; line-height: 24.6px; color: var(--text-blue);
  }
  .experience { position: absolute; left: 377px; top: 378px; width: 680px; }
  .experience h2 {
    font-weight: 400; font-size: 34px; line-height: 37px; color: var(--core-blue);
    margin-bottom: 24px;
  }
  .experience p, .experience li { font-size: 18.5px; line-height: 20.7px; color: var(--body-text); }
  .experience h3 { font-size: 18.5px; font-weight: 700; color: var(--body-text); margin: 20px 0 9px; }
  .experience ul { list-style: none; }
  .experience li { position: relative; padding-left: 33px; margin-bottom: 10px; }
  .experience li::before {
    content: ""; position: absolute; left: 3px; top: 6px;
    width: 10px; height: 10px; border-radius: 50%; background: #222;
  }
  .brand {
    position: absolute; left: 40px; top: 1176px; width: 225px; height: 167px;
    border: 2px solid var(--frame-gray);
    display: flex; align-items: center; justify-content: center;
  }
  .brand-name { font-weight: 700; font-size: 64px; letter-spacing: 6px; color: var(--core-blue); }
  .footer-gray { position: absolute; left: 0; top: 1365px; width: 306px; height: 62px; background: var(--cool-gray); }
  .footer-contact {
    position: absolute; left: 306px; top: 1365px; width: 821px; height: 62px;
    background: var(--core-blue); color: var(--white);
    font-family: "Roboto Condensed", "Arial Narrow", sans-serif; font-size: 21px;
  }
  .contact-item { position: absolute; top: 0; height: 62px; display: flex; align-items: center; gap: 14px; white-space: nowrap; }
  .contact-item svg { width: 32px; height: 32px; flex: none; }
  .contact-phone { left: 50px; }
  .contact-email { left: 278px; }
  .contact-web { left: 573px; }
</style>
</head>
<body>
<main class="sheet">
  <div class="wash"></div>

  <header>
    <div class="banner"><div class="banner-art" role="img" aria-label="Abstract blue geometric facets"></div></div>
    <div class="headshot" role="img" aria-label="Headshot photo of Daniel Mercer"></div>
    <h1 class="name">Daniel Mercer Textboxname</h1>
    <p class="role">Marketing Executive</p>
  </header>

  <p class="summary">Lorem ipsum dolor sit aamet, consectetur adipiscing eaalit. Quisque varius, mi sedabboa sedcondim entum graaaavida, ligula nunc maximus orci, sit amet mollis odio turpaaais et maris. Crasddd tempor mattis dictum. Vivaus interdum diam inlor emkkajjik mollis, atakjis tincdunt nullaaktab varius.aik Aliquam ut congquam. Seded pretium fringillabibendumaa cursus. Sed id ligula necasasa magna lacinia laoreet. Etiam id tempor velit. Phasellus sed dolor tincidunt, elementusam diam gravida, pharetra eros. Aenean diam dolor, laoreet ut lectus eu, eleife</p>

  <section class="experience">
    <h2>EXPERIENCES<br>PROFESSIONNELLES</h2>
    <p>Lorem ipsum dolor sit amet, consectetur adipiscing elit. Quisque varius, mi sed condimentum gravida, ligula nunc maximus orci, sit amet mollis odio turpis et mauris. Cras tempor mattis dictum. Vivamus interdum diam in lorem mollis, at tincidunt nulla varius. Aliquam ut congue quam. Sed pretium fringilla orci bibendum cursus. Sed id ligula nec magna lacinia laoreet. Etiam id tempor velit. Phasellus sed dolor tincidunt, elementum diam gravida, pharetra eros. Aenean diam dolor, laoreet ut lectus eu, eleifend varius urna. Etiam dictum ipsum quis hendrerit iaculis. Sed ut semper quam, sed consequat tortor. Curabitur ornare mollis eleifend. Quisque sem sem, efficitur luctus eros a, semper consequat arcu. Proin vel posuere quam, ut ultrices libero.</p>
    <h3>Lorem ipsum dolor sit amet, consectetur</h3>
    <ul>
      <li>Phasellus facilisis, nibh sed vestibulum semper, arcu turpis pellentesque est, eu mollis sem elit ac diam.</li>
      <li>In dictum velit eget nisl finibus euismod. Mauris aliquet finibus felis, ac vehicula quam maximus vitae. Maecenas ac dui eget elit tempor blandit auctor a lectus. Curabitur quis libero eu sem pretium placerat.</li>
      <li>Quisque maximus ligula velit, sit amet varius nisl interdum vel. Duis a ullamcorper massa, a pulvinar ante. Vivamus finibus odio sed ligula eleifend ullamcorper. Vivamus a iaculis diam. Aenean luctus dui in nunc sodales scelerisque.</li>
      <li>Phasellus tellus sem, egestas at erat quis, tincidunt fringilla nisi. Cras ultricies volutpat tortor.</li>
    </ul>
    <h3>Lorem ipsum dolor sit amet, consectetur</h3>
    <ul>
      <li>Phasellus facilisis, nibh sed vestibulum semper, arcu turpis pellentesque est, eu mollis sem elit ac diam.</li>
      <li>In dictum velit eget nisl finibus euismod. Mauris aliquet finibus felis, ac vehicula quam maximus vitae. Maecenas ac dui eget elit tempor blandit auctor a lectus. Curabitur quis libero eu sem pretium placerat.</li>
      <li>Quisque maximus ligula velit, sit amet varius nisl interdum vel. Duis a ullamcorper massa, a pulvinar ante. Vivamus finibus odio sed ligula eleifend ullamcorper. Vivamus a iaculis diam. Aenean luctus dui in nunc sodales scelerisque.</li>
      <li>Phasellus tellus sem, egestas at erat quis, tincidunt fringilla nisi. Cras ultricies volutpat tortor.</li>
    </ul>
  </section>

  <div class="brand"><span class="brand-name">KTW</span></div>

  <footer>
    <div class="footer-gray"></div>
    <div class="footer-contact">
      <div class="contact-item contact-phone">
        <svg viewBox="0 0 32 32" aria-hidden="true"><circle cx="16" cy="16" r="15" fill="#fff"/><path d="M11 8.5c1-.6 2-.3 2.5.6l1.5 2.8c.4.8.2 1.6-.5 2.1l-1 .8c.8 1.8 2.2 3.3 4 4.2l.8-1c.5-.7 1.4-.9 2.1-.5l2.8 1.5c.9.5 1.2 1.6.6 2.5l-.9 1.3c-.7 1-2 1.4-3.2 1-5-1.6-8.8-5.4-10.3-10.4-.4-1.2 0-2.5 1-3.1z" fill="var(--core-blue)"/></svg>
        <span>0098-7654-3210</span>
      </div>
      <div class="contact-item contact-email">
        <svg viewBox="0 0 32 32" aria-hidden="true"><circle cx="16" cy="16" r="14" fill="none" stroke="#fff" stroke-width="2"/><rect x="9" y="11" width="14" height="10" fill="none" stroke="#fff" stroke-width="1.8"/><path d="M9 11l7 6 7-6" fill="none" stroke="#fff" stroke-width="1.8"/></svg>
        <span>hello@ktwoffice.com</span>
      </div>
      <div class="contact-item contact-web">
        <svg viewBox="0 0 32 32" aria-hidden="true"><g fill="none" stroke="#fff" stroke-width="1.8"><circle cx="16" cy="16" r="13"/><ellipse cx="16" cy="16" rx="6" ry="13"/><path d="M3 16h26M5 9.5h22M5 22.5h22M16 3v26"/></g></svg>
        <span>www.ktwoffice.com</span>
      </div>
    </div>
  </footer>
</main>
</body>
</html>
```